BrimWay

This app is built around three game modes—Quick Focus, Daily, and Calming—each offering short, low-stress interactions designed to prime focus, train cognitive skills, or regulate anxiety using neuroscience-informed mechanics. Gameplay spans spatial puzzles, word and memory challenges, and breathing or sensory experiences, all delivered in 1–5 minute routines with clean, calming UI patterns (grids, cards, breathing rings, soft animations). The goal is a cohesive system of micro-games and guided routines that enhance executive function, emotional regulation, and readiness before, during, or after high-stakes moments.

Colors
FFC000
F8CF3A
FAE287
FDF2CF
FEFAEE
F0912C
F2A743
F7CA91
FBE8D2
FDF5EE
EE7325
F08F49
F5BC92
FAE3D3
FDF4ED

```html
<!DOCTYPE html>
<html lang="en">
<head>
<meta charset="UTF-8">
<title>BrimWay – Welcome</title>
<link href="https://fonts.googleapis.com/css2?family=Outfit:wght@400;600;800&display=swap" rel="stylesheet">
<style>
  :root {
    --cream: #F5ECE2;
    --band: #F6E8C4;
    --ink: #3B2F1C;
    --orange: #EE7325;
    --orange-soft: #F5A27A;
    --orange-deep: #F47A22;
    --white: #FFFFFF;
    --chip: #F7F3F1;
  }
  * { margin: 0; padding: 0; box-sizing: border-box; }
  html, body {
    width: 677px;
    height: 1200px;
    overflow: hidden;
    background: var(--cream);
  }
  .welcome-screen {
    position: relative;
    width: 677px;
    height: 1200px;
    background: var(--cream);
    font-family: "Outfit", sans-serif;
    color: var(--ink);
    overflow: hidden;
  }
  .backdrop-band {
    position: absolute;
    inset: 0;
    width: 677px;
    height: 1200px;
  }
  .status-bar {
    position: absolute;
    top: 22px;
    left: 0;
    width: 100%;
    padding: 0 44px 0 56px;
    display: flex;
    justify-content: space-between;
    align-items: center;
    font-weight: 600;
    font-size: 22px;
  }
  .status-icons { display: flex; gap: 8px; align-items: center; }
  .brand {
    position: absolute;
    top: 500px;
    left: 0;
    width: 100%;
    display: flex;
    justify-content: center;
    align-items: center;
    gap: 16px;
  }
  .brand-dot {
    width: 70px;
    height: 70px;
    border-radius: 50%;
    background: var(--orange);
  }
  .brand-name {
    font-weight: 800;
    font-size: 96px;
    line-height: 1;
    letter-spacing: -1px;
    color: var(--ink);
  }
  .tagline {
    position: absolute;
    top: 628px;
    left: 0;
    width: 100%;
    text-align: center;
    font-size: 26px;
    font-weight: 400;
  }
  .begin-button {
    position: absolute;
    left: 63px;
    top: 985px;
    width: 551px;
    height: 88px;
    border-radius: 44px;
    background: linear-gradient(100deg, var(--orange-soft) 0%, var(--orange-soft) 35%, var(--orange-deep) 78%, var(--orange-deep) 100%);
    display: flex;
    align-items: center;
    justify-content: center;
    color: var(--white);
    font-weight: 600;
    font-size: 26px;
  }
  .begin-arrow {
    position: absolute;
    right: 12px;
    top: 11px;
    width: 66px;
    height: 66px;
    border-radius: 50%;
    background: var(--chip);
    display: flex;
    align-items: center;
    justify-content: center;
  }
</style>
</head>
<body>
<main class="welcome-screen">
  <svg class="backdrop-band" viewBox="0 0 677 1200" aria-hidden="true">
    <path fill="var(--band)" d="M377 0 L677 0 L677 574 C500 760 200 1000 49 1200 L0 1200 L0 1045 C150 820 380 560 470 380 C540 230 480 80 377 0 Z"/>
  </svg>

  <div class="status-bar">
    <span class="status-time">9:41</span>
    <span class="status-icons">
      <svg width="24" height="16" viewBox="0 0 24 16" aria-hidden="true">
        <rect x="0" y="11" width="4" height="5" rx="1" fill="var(--ink)"/>
        <rect x="6" y="8" width="4" height="8" rx="1" fill="var(--ink)"/>
        <rect x="12" y="4" width="4" height="12" rx="1" fill="var(--ink)"/>
        <rect x="18" y="0" width="4" height="16" rx="1" fill="var(--ink)"/>
      </svg>
      <svg width="22" height="16" viewBox="0 0 22 16" aria-hidden="true">
        <path d="M1 5 A14 14 0 0 1 21 5" fill="none" stroke="var(--ink)" stroke-width="2.5" stroke-linecap="round"/>
        <path d="M5 9 A8 8 0 0 1 17 9" fill="none" stroke="var(--ink)" stroke-width="2.5" stroke-linecap="round"/>
        <circle cx="11" cy="13.5" r="2.3" fill="var(--ink)"/>
      </svg>
      <svg width="32" height="16" viewBox="0 0 32 16" aria-hidden="true">
        <rect x="1" y="1" width="26" height="14" rx="4" fill="none" stroke="var(--ink)" stroke-width="1.5"/>
        <rect x="3.5" y="3.5" width="21" height="9" rx="2" fill="var(--ink)"/>
        <rect x="28.5" y="5.5" width="2.5" height="5" rx="1" fill="var(--ink)"/>
      </svg>
    </span>
  </div>

  <div class="brand">
    <span class="brand-dot"></span>
    <span class="brand-name">BrimWay</span>
  </div>

  <p class="tagline">Focus better. Feel calmer. Perform smarter.</p>

  <div class="begin-button">
    <span class="begin-label">Begin Session</span>
    <span class="begin-arrow">
      <svg width="24" height="18" viewBox="0 0 24 18" aria-hidden="true">
        <path d="M2 9 H21 M14 2 L21 9 L14 16" fill="none" stroke="var(--ink)" stroke-width="2" stroke-linecap="round" stroke-linejoin="round"/>
      </svg>
    </span>
  </div>
</main>
</body>
</html>
```